Gorgeous A5 Booklet 8pp - Existing Branding

Please transform a PDF text doc into an A5 booklet according to my existing branding, I need it fast.
I need to go to print.
Must be modern, fun, clean and classy design.
I can send images, logos and the .indd for the existing pdf to help you.
Thanks for being awesome!

We are a design agency so it needs to be good...we are too busy to create it.

Front cover can have open paragraph.
Back cover must have contact details
three inside spreads should have the 11 essentials.

The executive summary attached is a good example of the look and feel you can copy.

Please let me know if you have any questions.
Thanks
Light ahead!
:)

Target Market(s)

entreprenuers and small business owners

Industry/Entity Type

Design Agency

Font styles to use
Sans Serif

Colors
e34197
fff5ee
333333
faa54b
acd036
33a6d7

Requirements
Must have
• font is century gothic - no bold
gudea body text
sketch rockwell
seans hand

see website www.tidelantern.com.au for branding
or match to pdf attached with origami images

Colours in palette below of only indicative. actual colours are as per website colour strip.
Should not have
• not too pink
not too many stars

```html
<!DOCTYPE html>
<html lang="en">
<head>
<meta charset="utf-8">
<title>Tidelantern booklet – back and front cover</title>
<link href="https://fonts.googleapis.com/css2?family=Questrial&family=Gudea:wght@400;700&family=Arvo:wght@400;700&display=swap" rel="stylesheet">
<style>
  :root {
    --desk: #3b3b3b;
    --paper: #ffffff;
    --linen: #e5e2de;
    --linen-edge: #dcd8d3;
    --label-grey: #e3e3e3;
    --ink: #333333;
    --ink-soft: #555555;
    --pink: #e34197;
    --blue: #33a6d7;
    --teal: #3a9a9c;
    --green: #acd036;
    --orange: #f07a3a;
    --brand-grey: #8c8c8c;
  }
  * { margin: 0; padding: 0; box-sizing: border-box; }
  html, body { width: 1200px; height: 738px; overflow: hidden; }
  body { background: var(--desk); position: relative; font-family: "Gudea", sans-serif; color: var(--ink); }

  .page { position: absolute; top: 0; width: 521px; height: 738px; background: var(--paper); overflow: hidden; }
  .page--back { left: 10px; }
  .page--front { left: 636px; }

  .colour-strip { position: absolute; left: 0; right: 0; top: 638px; height: 6px; display: flex; }
  .colour-strip span { flex: 1; }
  .colour-strip .teal { background: var(--teal); }
  .colour-strip .pink { background: var(--pink); }
  .colour-strip .green { background: var(--green); }
  .colour-strip .orange { background: var(--orange); }

  .brand-name { position: absolute; left: 18px; top: 693px; display: flex; align-items: center; gap: 6px;
    font-family: "Questrial", sans-serif; font-size: 26px; color: var(--brand-grey); letter-spacing: 0.5px; }
  .brand-name .dot { width: 12px; height: 12px; border-radius: 50%; background: var(--brand-grey); }

  /* back cover */
  .linen-edge { position: absolute; left: 0; top: 0; width: 42px; height: 638px; background: var(--linen-edge); }
  .title-tab { position: absolute; left: 0; top: 41px; width: 42px; height: 61px; background: var(--pink); }
  .page-title { position: absolute; left: 45px; top: 44px; font-family: "Questrial", sans-serif; font-size: 31px; font-weight: 400; color: #111; }

  .section-label { position: absolute; left: 257px; width: 264px; height: 50px; background: var(--label-grey);
    font-family: "Questrial", sans-serif; font-size: 20.5px; font-weight: 400; color: var(--blue); padding: 12px 0 0 12px; }
  .section-label::after { content: ""; position: absolute; right: 0; top: 0; width: 18px; height: 100%; background: var(--pink); }
  .section-label--support { top: 101px; }
  .section-label--contact { top: 355px; }

  .support-name { position: absolute; left: 274px; top: 160px; font-family: "Questrial", sans-serif; font-size: 16.5px; color: var(--pink); }
  .support-copy { position: absolute; left: 257px; top: 189px; width: 255px; font-family: "Questrial", sans-serif; font-size: 13.8px; line-height: 22px; color: var(--ink); }
  .support-copy .hours { margin-top: 12px; line-height: 17px; }
  .support-copy .days { margin-top: 7px; }

  .contact-list { position: absolute; left: 257px; top: 413px; list-style: none; font-family: "Questrial", sans-serif; font-size: 14px; line-height: 22.5px; color: var(--ink-soft); }

  /* front cover */
  .linen { position: absolute; left: 0; top: 0; width: 521px; height: 638px; background: var(--linen); }
  .frame-line { position: absolute; background: var(--green); }
  .frame-line--top { left: 46px; top: 41px; width: 272px; height: 2px; }
  .frame-line--bottom { left: 321px; top: 468px; width: 184px; height: 2px; }
  .frame-line--bottom-drop { left: 503px; top: 468px; width: 2px; height: 30px; }

  .cover-kicker { position: absolute; left: 66px; top: 53px; font-family: "Arvo", serif; font-weight: 700; font-size: 25px; color: var(--blue); }
  .cover-title { position: absolute; left: 64px; top: 90px; font-family: "Arvo", serif; font-weight: 700; font-size: 59px; line-height: 64px; color: var(--pink); }
  .cover-title .line2 { display: block; padding-left: 2px; }
  .cover-intro { position: absolute; left: 27px; top: 229px; width: 440px; font-family: "Gudea", sans-serif; font-weight: 400; font-size: 14.8px; line-height: 30px; color: var(--ink); white-space: nowrap; }

  .icon-badge { position: absolute; left: 353px; top: 483px; width: 139px; height: 139px; border-radius: 50%; background: var(--paper); }

  .origami { position: absolute; top: 672px; height: 56px; }
  .origami--butterfly { left: 232px; width: 68px; border-radius: 40% 60% 45% 55%; background: linear-gradient(135deg, #f9b23a, #f08a1c); }
  .origami--elephant { left: 318px; width: 74px; border-radius: 45% 45% 30% 30%; background: linear-gradient(135deg, #9fd04a, #4f9e35); }
  .origami--boat { left: 412px; top: 684px; width: 96px; height: 40px; border-radius: 10% 10% 50% 50%; background: linear-gradient(135deg, #8fd3f3, #2c9ad6); }
</style>
</head>
<body>

  <section class="page page--back" aria-label="Back cover: contact details">
    <div class="linen-edge"></div>
    <div class="title-tab"></div>
    <h1 class="page-title">contact us</h1>

    <h2 class="section-label section-label--support">online support centre</h2>
    <p class="support-name">Tidelantern Support Centre</p>
    <div class="support-copy">
      <p>Submit a ticket via our support<br>centre for prompt service. This will<br>log your request in the queue and<br>we will address it ASAP.</p>
      <p class="hours">Email and phone support is avail-<br>able 9am - 5pm AEST</p>
      <p class="days">Mon - Fri</p>
    </div>

    <h2 class="section-label section-label--contact">contact us</h2>
    <ul class="contact-list">
      <li>Phone: 1300 482 615</li>
      <li>Land Line: 02 9418 3356</li>
      <li>info@tidelantern.com.au</li>
      <li>Fax: 02 9418 3390</li>
      <li>Tidelantern Pty Ltd</li>
      <li>ACN 204 771 086</li>
    </ul>

    <div class="colour-strip"><span class="teal"></span><span class="pink"></span><span class="green"></span><span class="orange"></span></div>
    <div class="brand-name"><span>tidelantern</span><span class="dot"></span></div>
  </section>

  <section class="page page--front" aria-label="Front cover">
    <div class="linen"></div>
    <div class="frame-line frame-line--top"></div>
    <div class="frame-line frame-line--bottom"></div>
    <div class="frame-line frame-line--bottom-drop"></div>

    <p class="cover-kicker">11 Essentials for a</p>
    <h1 class="cover-title">Successful<span class="line2">website</span></h1>
    <p class="cover-intro">Your website is an essential part of your business, it is important<br>to give it the attention it deserves. We repeatedly see good<br>websites deliver excellent results for small businesses which<br>would previously have wasted a lot of time and money on<br>ineffective marketing. Read the report below about the<br>11 essential elements we have seen work magic on small<br>business websites.</p>

    <div class="icon-badge" role="img" aria-label="Pink laptop icon in a white circle"></div>

    <div class="colour-strip"><span class="teal"></span><span class="pink"></span><span class="green"></span><span class="orange"></span></div>
    <div class="brand-name"><span>tidelantern</span><span class="dot"></span></div>

    <div class="origami origami--butterfly" role="img" aria-label="Orange paper origami butterfly"></div>
    <div class="origami origami--elephant" role="img" aria-label="Green paper origami elephant"></div>
    <div class="origami origami--boat" role="img" aria-label="Blue paper origami boat"></div>
  </section>

</body>
</html>
```